Invitation for end of year celebration and moving up ceremony/graduatio

Create an invitation template to be used for a fifth grade moving up end of year event. The theme for the event is sports and we will be using a graphic like the attached.

Details subject to change but current details to be included on event are as follows:
Event Date June 12, 2020 6 PM - 9:15 PM
Fifth Graders arrive 6PM
Parents arrive 8:30 PM for family photos and video presentation
Event Name: Maple Crest Falcon Trials
You are invited to Maple Crest Stadium for the Falcon Trials!

Uploaded file includes a sample from a prior year's event (Pinecone file). and the graphic logo to be included on the event this year.

Target Market(s)

11 year old boys and girls and their parents. The event is to celebrate the children's last year at their elementary school as they move up to middle school. (Grade 6).

Industry/Entity Type

School

Colors
0456a4
0792cd
ffffff
fbee3e
ec1f27

Requirements
Must have
• include 1 or 2 of the graphics attached - at least 1 must be a stadium graphic.
• Invitation will be printed on approximately 8x4 or 9x4 card stock for ticket like invites. so the file needs to be created in a way that will allow adjusting for printing/bleedlines and cut lines.
Nice to have
• Some ideas I would like to see are to make it look like a ticket for a sporting event .

```html
<!DOCTYPE html>
<html lang="en">
<head>
<meta charset="utf-8">
<title>Maple Crest Falcon Trials – Ticket Invitation</title>
<link rel="stylesheet" href="https://fonts.googleapis.com/css2?family=Montserrat:wght@600;700;800&family=Staatliches&display=swap">
<style>
  :root {
    --blue-deep: #2b63ad;
    --blue-bright: #0792cd;
    --navy: #1c1c2e;
    --yellow: #f2ea1f;
    --red: #9b1b22;
    --white: #ffffff;
    --ink: #111111;
  }
  * { box-sizing: border-box; margin: 0; padding: 0; }
  html, body { width: 1200px; height: 622px; overflow: hidden; background: var(--white); }
  body { position: relative; font-family: "Montserrat", sans-serif; }

  .ticket {
    position: absolute; left: 86px; top: 88px; width: 1010px; height: 448px;
    border: 1px solid var(--navy); overflow: hidden;
  }

  /* Stub */
  .stub {
    position: absolute; left: 0; top: 0; width: 264px; height: 100%;
    background: var(--blue-deep); text-align: center; color: var(--white);
  }
  .stub__tab { position: absolute; left: 64px; top: 0; width: 146px; height: 30px; background: var(--yellow); }
  .stub__label {
    position: absolute; left: 0; top: 30px; width: 100%; height: 30px; background: var(--white);
    color: var(--blue-deep); font-weight: 800; font-size: 17px; letter-spacing: 1px; line-height: 30px;
  }
  .stub__date {
    position: absolute; left: 64px; top: 62px; width: 146px; height: 136px;
    background: var(--yellow); color: var(--ink);
    clip-path: polygon(0 0, 100% 0, 100% 100%, 50% 90%, 0 100%);
  }
  .stub__day { font-weight: 700; font-size: 16px; padding-top: 8px; }
  .stub__rule { width: 120px; height: 1px; background: var(--ink); margin: 4px auto 2px; }
  .stub__time { font-weight: 800; font-size: 27px; line-height: 31px; }
  .stub__dash { width: 16px; height: 3px; background: var(--ink); margin: 1px auto 3px; }
  .stub__notes { position: absolute; left: 0; top: 210px; width: 100%; font-weight: 700; font-size: 13.5px; line-height: 18.5px; }
  .stub__dots { width: 150px; margin: 6px auto; border-top: 3px dotted var(--white); }
  .stub__admit {
    position: absolute; left: 0; top: 386px; width: 100%;
    font-family: "Staatliches", sans-serif; font-size: 50px; color: var(--yellow); letter-spacing: 1px; line-height: 50px;
  }
  .perforation { position: absolute; left: 264px; top: 0; height: 100%; border-left: 3px dotted var(--navy); }

  /* Main panel */
  .main { position: absolute; left: 267px; top: 0; right: 0; height: 100%; }
  .main__rays { position: absolute; inset: 0; background: radial-gradient(circle at 58% 55%, #f6ef4a 0%, var(--yellow) 60%, #e3da1a 100%); }
  .card { position: absolute; left: 31px; top: 36px; width: 652px; height: 364px; }
  .card__frame { position: absolute; inset: 0; }
  .card__invite {
    position: absolute; left: 0; top: 18px; width: 100%; text-align: center;
    color: var(--blue-deep); font-weight: 700; font-size: 16px;
  }
  .card__art {
    position: absolute; left: 80px; top: 44px; width: 504px; height: 290px; border-radius: 8px;
    background: radial-gradient(ellipse at 50% 45%, #f4b2a0 0%, #c8464a 40%, #3f63b8 75%, #ffffff 100%);
  }
  .banner { position: absolute; left: 40px; top: 370px; width: 572px; height: 54px; }
  .banner__text {
    position: absolute; left: 0; top: 0; width: 100%; height: 100%; text-align: center;
    font-family: "Staatliches", sans-serif; font-size: 40px; line-height: 54px; letter-spacing: 2px;
    color: var(--blue-bright);
  }
</style>
</head>
<body>
  <div class="ticket">
    <section class="stub">
      <div class="stub__tab"></div>
      <div class="stub__label">EVENT DATE</div>
      <div class="stub__date">
        <div class="stub__day">June 12, 2020</div>
        <div class="stub__rule"></div>
        <div class="stub__time">6:00 PM</div>
        <div class="stub__dash"></div>
        <div class="stub__time">9:15 PM</div>
      </div>
      <div class="stub__notes">
        <p>FIFTH GRADERS<br>ARRIVE 6PM</p>
        <div class="stub__dots"></div>
        <p>PARENTS ARRIVE<br>8:30 PM FOR<br>FAMILY PHOTOS<br>AND VIDEO<br>PRESENTATION</p>
        <div class="stub__dots"></div>
      </div>
      <div class="stub__admit">ADMIT ONE</div>
    </section>
    <div class="perforation"></div>

    <section class="main">
      <div class="main__rays" role="img" aria-label="Blue and yellow sunburst rays radiating from the centre"></div>
      <div class="card">
        <svg class="card__frame" width="652" height="364" viewBox="0 0 652 364">
          <path d="M20 0H632A20 20 0 0 0 652 20V344A20 20 0 0 0 632 364H20A20 20 0 0 0 0 344V20A20 20 0 0 0 20 0Z" fill="#ffffff" stroke="#9b1b22" stroke-width="3"/>
          <path d="M26 8H626A18 18 0 0 0 644 26V338A18 18 0 0 0 626 356H26A18 18 0 0 0 8 338V26A18 18 0 0 0 26 8Z" fill="none" stroke="#9b1b22" stroke-width="2" stroke-dasharray="1 4" stroke-linecap="round"/>
        </svg>
        <p class="card__invite">You are invited to Maple Crest Stadium for the Falcon Trials!</p>
        <div class="card__art" role="img" aria-label="Stadium illustration with 2020 graduation cap, trophy, two cheering cartoon students and sports balls"></div>
      </div>
      <div class="banner">
        <svg width="572" height="54" viewBox="0 0 572 54">
          <polygon points="0,0 572,0 560,27 572,54 0,54 12,27" fill="#9b1b22"/>
        </svg>
        <div class="banner__text">MAPLE CREST FALCON TRIALS</div>
      </div>
    </section>
  </div>
</body>
</html>
```